The billboard should communicate confidence, energy and approachability while maintaining a professional, premium feel. Rather than relying on a standard agent photograph, property collage or crowded list of services, we would like an original creative idea that makes people look twice. This could involve a fun visual, clever headline, striking colour contrast or an unexpected real estate theme. The concept should feel positive and contemporary, with enough personality to become recognisable throughout the local community.

The key message should appeal to homeowners who are thinking about selling, preparing to sell or simply curious about the value of their property. Copy must be short, clear and conversational, supported by a direct call to action. The agent’s name, phone number and company branding should remain highly visible without competing with the main idea.

The finished billboard will measure 8.0 metres wide by 2.08 metres high (1224px x 324px), so the composition must suit a long landscape format. All important text and imagery should remain comfortably within safe margins and be legible from a distance. The design should avoid small writing, unnecessary detail and visual clutter.

The goal is to create a billboard that feels different from every other real estate sign in the area—something engaging, confident and easy to remember. It should build strong brand awareness, generate conversations and encourage local property owners to contact the agent when they are ready to make their next move. The concept should be adaptable for future campaigns, helping establish a consistent, distinctive and trusted local brand presence.

Target Market(s)

ages 30+

Industry/Entity Type

Real Estate

Requirements
Must have
• call Wade and phone number 0417 63 28 05
Nice to have
• Nice bright and yellow.. Exciting and grabbing

```html
<!DOCTYPE html>
<html lang="en">
<head>
<meta charset="utf-8">
<title>What's Yours Worth? – Call Wade</title>
<link href="https://fonts.googleapis.com/css2?family=Montserrat:wght@600;700;800;900&family=Roboto+Condensed:wght@700&display=swap" rel="stylesheet">
<style>
  :root {
    --yellow: #ffe002;
    --yellow-deep: #f2cf00;
    --ink: #111111;
    --graphite: #3a3a3a;
    --white: #ffffff;
  }
  * { margin: 0; padding: 0; box-sizing: border-box; }
  html, body { width: 1200px; height: 512px; overflow: hidden; background: var(--yellow); }
  .billboard {
    position: relative;
    width: 1200px;
    height: 512px;
    background: var(--yellow);
    font-family: "Montserrat", sans-serif;
    color: var(--ink);
    overflow: hidden;
  }

  /* Headline */
  .headline { font-weight: 900; line-height: 1; }
  .headline span { position: absolute; display: block; white-space: nowrap; transform-origin: left top; }
  .headline .line-whats { left: 59px; top: 23px; font-size: 89px; letter-spacing: -3px; color: var(--ink); transform: scaleX(0.94); }
  .headline .line-yours { left: 53px; top: 88px; font-size: 134px; letter-spacing: -2px; color: var(--graphite); transform: scaleX(1.27); }
  .headline .line-worth { left: 66px; top: 226px; font-size: 124px; letter-spacing: -1px; color: var(--ink); }

  /* Prompt line */
  .prompt {
    position: absolute;
    left: 159px;
    top: 346px;
    width: 466px;
    display: flex;
    align-items: center;
    gap: 18px;
    font-weight: 700;
    font-size: 25px;
    line-height: 1;
    white-space: nowrap;
  }
  .prompt::before, .prompt::after {
    content: "";
    flex: 1;
    height: 2px;
    background: var(--ink);
  }

  /* Call to action band */
  .call-band {
    position: absolute;
    left: 31px;
    top: 378px;
    width: 752px;
    height: 106px;
    z-index: 2;
  }
  .call-band svg.band-shape { position: absolute; inset: 0; }
  .call-icon { position: absolute; left: 31px; top: 11px; }
  .call-label {
    position: absolute;
    left: 128px;
    top: 15px;
    line-height: 1;
    font-weight: 800;
  }
  .call-label .call-word { display: block; font-size: 29px; color: var(--white); }
  .call-label .call-name { display: block; font-size: 45px; color: var(--yellow); margin-top: 2px; letter-spacing: -1px; }
  .call-divider {
    position: absolute;
    left: 280px;
    top: 17px;
    width: 2px;
    height: 72px;
    background: var(--white);
  }
  .call-number {
    position: absolute;
    left: 306px;
    top: 22px;
    font-family: "Roboto Condensed", sans-serif;
    font-weight: 700;
    font-size: 66px;
    line-height: 1;
    color: var(--white);
    letter-spacing: -0.5px;
    white-space: nowrap;
  }

  /* Hero visual area */
  .hero-visual {
    position: absolute;
    left: 760px;
    top: 25px;
    width: 232px;
    height: 427px;
    background: radial-gradient(ellipse at 50% 50%, #1c1c1c 0%, #1c1c1c 40%, rgba(28,28,28,0) 72%);
    z-index: 1;
  }

  /* Slogan */
  .slogan {
    position: absolute;
    left: 1025px;
    top: 86px;
    width: 130px;
    font-weight: 700;
    font-size: 20px;
    line-height: 1.6;
    color: var(--ink);
    transform: rotate(-3deg);
    transform-origin: left top;
  }
  .slogan-line { display: block; padding-bottom: 8px; margin-bottom: 14px; border-bottom: 3px solid var(--ink); }
  .slogan-line.second { width: 104px; }

  /* Brand */
  .brand {
    position: absolute;
    left: 926px;
    top: 396px;
    width: 230px;
    text-align: center;
  }
  .brand-name {
    display: block;
    font-weight: 800;
    font-size: 33px;
    line-height: 1;
    color: var(--graphite);
    letter-spacing: -1px;
  }
  .brand-tagline {
    display: block;
    margin-top: 16px;
    font-weight: 700;
    font-size: 11px;
    letter-spacing: 0.3px;
    color: var(--ink);
    white-space: nowrap;
  }
</style>
</head>
<body>
  <main class="billboard">
    <h1 class="headline">
      <span class="line-whats">WHAT’S</span>
      <span class="line-yours">YOURS</span>
      <span class="line-worth">WORTH?</span>
    </h1>

    <p class="prompt">Curious? Let’s find out.</p>

    <div class="call-band">
      <svg class="band-shape" width="752" height="106" viewBox="0 0 752 106" aria-hidden="true">
        <path d="M14 10 L44 3 L420 4 L690 8 L748 16 L724 28 L746 42 L718 56 L744 72 L706 88 L560 102 L120 104 L22 100 L4 86 L16 68 L0 52 L14 34 L2 20 Z" fill="#111111"/>
      </svg>
      <svg class="call-icon" width="82" height="82" viewBox="0 0 82 82" aria-hidden="true">
        <circle cx="41" cy="41" r="37" fill="none" stroke="#ffe002" stroke-width="5"/>
        <path d="M29 23 c3-2 6-1 7 2 l3 7 c1 2 0 4-2 5 l-3 2 c2 5 6 9 11 11 l2-3 c1-2 3-3 5-2 l7 3 c3 1 4 4 2 7 l-3 4 c-3 3-8 3-13 1 c-9-4-17-12-21-21 c-2-5-2-10 1-13 Z" fill="none" stroke="#ffe002" stroke-width="3.5" stroke-linejoin="round"/>
      </svg>
      <div class="call-label">
        <span class="call-word">CALL</span>
        <span class="call-name">WADE</span>
      </div>
      <div class="call-divider"></div>
      <div class="call-number">0417 63 28 05</div>
    </div>

    <div class="hero-visual" role="img" aria-label="Bold black 3D question mark whose top outline forms a house roof with chimney and small window"></div>

    <p class="slogan">
      <span class="slogan-line">Local Knowledge.</span>
      <span class="slogan-line second">Real Results.</span>
    </p>

    <div class="brand">
      <span class="brand-name">Lorne Bexley</span>
      <span class="brand-tagline">YOUR LOCAL REAL ESTATE EXPERT</span>
    </div>
  </main>
</body>
</html>
```